Business card design for Bront Engineering Qavo

We need a new business card design along with all the necessary to place an order. The company is Bront Engineering Qavo and we recently updated our logo.

```html
<!DOCTYPE html>
<html lang="en">
<head>
<meta charset="utf-8">
<title>Bront Engineering Qavo – Business Card</title>
<link href="https://fonts.googleapis.com/css2?family=Kanit:wght@400;600;700&display=swap" rel="stylesheet">
<style>
  :root {
    --backdrop: #3a3a3c;
    --card-dark: #1e1e1f;
    --card-light: #989896;
    --brand-grey: #9a9a9a;
    --brand-light: #d4d4d4;
    --accent: #e3bf27;
    --text-light: #f2f2f2;
  }
  * { margin: 0; padding: 0; box-sizing: border-box; }
  html, body {
    width: 1200px; height: 1059px; overflow: hidden;
    background: var(--backdrop);
    font-family: "Kanit", sans-serif;
  }
  .canvas { position: relative; width: 1200px; height: 1059px; }

  .card { position: absolute; border-radius: 18px; }
  .card--front { left: 257px; top: 100px; width: 687px; height: 392px; background: var(--card-dark); }
  .card--back  { left: 253px; top: 536px; width: 694px; height: 396px; background: var(--card-light); }

  .wordmark {
    position: absolute; left: 0; right: 0;
    display: flex; align-items: center; justify-content: center; gap: 18px;
    font-weight: 600; line-height: 1;
  }
  .wordmark__square { width: 22px; height: 22px; flex: none; }
  .wordmark__text { display: flex; flex-direction: column; align-items: flex-start; }
  .wordmark__main { font-size: 80px; letter-spacing: 6px; }
  .wordmark__sub { font-size: 31px; letter-spacing: 2px; margin-top: 4px; }

  .card--front .wordmark { top: 30px; color: var(--brand-grey); }
  .card--front .wordmark__square { background: var(--accent); }
  .card--back .wordmark { top: 128px; color: var(--brand-light); }
  .card--back .wordmark__square { background: var(--brand-light); }

  .person {
    position: absolute; right: 387px; top: 214px; text-align: right;
  }
  .person__name { font-size: 30px; font-weight: 700; color: var(--accent); line-height: 1.1; letter-spacing: -0.3px; }
  .person__role { font-size: 17px; font-weight: 400; color: var(--text-light); margin-top: 6px; }

  .divider { position: absolute; left: 327px; top: 216px; width: 2px; height: 70px; background: var(--accent); }

  .contacts { position: absolute; left: 355px; top: 211px; list-style: none; }
  .contacts__item {
    display: flex; align-items: center; gap: 8px;
    font-size: 17px; color: var(--text-light); height: 27px;
  }
  .contacts__icon { width: 15px; height: 15px; flex: none; fill: var(--accent); }

  .address {
    position: absolute; left: 0; right: 0; top: 338px; text-align: center;
    font-size: 17px; color: var(--text-light);
  }
</style>
</head>
<body>
<main class="canvas">
  <section class="card card--front">
    <div class="wordmark">
      <span class="wordmark__square"></span>
      <div class="wordmark__text">
        <span class="wordmark__main">BRONT</span>
        <span class="wordmark__sub">ENGINEERING QAVO</span>
      </div>
    </div>

    <div class="person">
      <p class="person__name">DANIEL HARTLEY</p>
      <p class="person__role">Managing Director</p>
    </div>

    <span class="divider"></span>

    <ul class="contacts">
      <li class="contacts__item">
        <svg class="contacts__icon" viewBox="0 0 16 16" aria-hidden="true"><path d="M1 6c0-2 3-3 7-3s7 1 7 3v1h-3V5.5H4V7H1zM3 8h10l1 6H2zM6 10a2 2 0 1 0 4 0a2 2 0 1 0-4 0z"/></svg>
        01632 960482
      </li>
      <li class="contacts__item">
        <svg class="contacts__icon" viewBox="0 0 16 16" aria-hidden="true"><path d="M1 4h14v1l-7 4.5L1 5zM1 6.5l7 4.5 7-4.5V13H1z"/></svg>
        sales@brontengineering.co.uk
      </li>
      <li class="contacts__item">
        <svg class="contacts__icon" viewBox="0 0 16 16" aria-hidden="true"><circle cx="8" cy="8" r="7"/><path d="M4 4c2 1 1 3 3 3s1 3 0 4M10 3c-1 2 2 3 3 2M10 12c1-2 3-2 4-1" stroke="#1e1e1f" stroke-width="1.2" fill="none"/></svg>
        www.brontengineering.co.uk
      </li>
    </ul>

    <p class="address">Bront Engineering Qavo 22b Farrow Lane, Kettering NN15 4TR</p>
  </section>

  <section class="card card--back">
    <div class="wordmark">
      <span class="wordmark__square"></span>
      <div class="wordmark__text">
        <span class="wordmark__main">BRONT</span>
        <span class="wordmark__sub">ENGINEERING QAVO</span>
      </div>
    </div>
  </section>
</main>
</body>
</html>
```